Business Card

The design you sent was fine. I just need the logo changed on one side. The back needs to have the text "Vela Norquist Group" next to the log and the words "Advice Acumen Advocacy" in the middle. The front logo needs to have the "Vela Norquist Advisory" logo attached

Colors

Designer to choose colors to be used in the design.

```html
<!DOCTYPE html>
<html lang="en">
<head>
<meta charset="utf-8">
<title>Vela Norquist – Business Card</title>
<link rel="stylesheet" href="https://fonts.googleapis.com/css2?family=Montserrat:wght@400;600;700&family=Open+Sans:wght@600;700&display=swap">
<style>
  :root {
    --stage: #2b2b2c;
    --ink: #1b1b1c;
    --paper: #ffffff;
    --cyan: #22b3e0;
  }
  * { box-sizing: border-box; margin: 0; padding: 0; }
  html, body { width: 1200px; height: 880px; overflow: hidden; }
  body {
    background: var(--stage);
    font-family: "Montserrat", sans-serif;
    position: relative;
  }
  .card {
    position: absolute;
    left: 300px;
    width: 600px;
    height: 340px;
    border-radius: 20px;
    overflow: hidden;
  }

  /* Back: white group card */
  .card--back { top: 80px; background: var(--paper); color: var(--ink); }
  .group-brand {
    position: absolute; left: 56px; top: 104px;
    display: flex; align-items: center; gap: 18px;
  }
  .group-brand__dot {
    width: 48px; height: 48px; border-radius: 50%;
    background: var(--cyan); flex: none;
  }
  .group-brand__name {
    font-family: "Open Sans", sans-serif; font-weight: 700;
    font-size: 40px; letter-spacing: -0.5px; line-height: 1;
  }
  .group-brand__tagline {
    position: absolute; left: 122px; top: 168px;
    font-size: 16px; letter-spacing: 0.5px;
  }
  .group-pillars {
    position: absolute; left: 56px; bottom: 56px;
    font-size: 17px; letter-spacing: 2px;
  }
  .group-pillars strong { font-weight: 700; }

  /* Front: dark advisory card */
  .card--front { top: 460px; background: var(--ink); color: var(--paper); }
  .advisory-brand {
    position: absolute; left: 50px; top: 52px;
    display: flex; align-items: center; gap: 20px;
  }
  .advisory-brand__dot {
    width: 66px; height: 66px; border-radius: 50%;
    background: var(--cyan); flex: none;
  }
  .advisory-brand__name {
    font-family: "Open Sans", sans-serif; font-weight: 700;
    font-size: 40px; line-height: 1; letter-spacing: -0.5px;
  }
  .advisory-brand__sub {
    display: flex; align-items: center; gap: 10px; margin-top: 6px;
    font-size: 15px; font-weight: 700; letter-spacing: 3px;
  }
  .advisory-brand__sub::before,
  .advisory-brand__sub::after {
    content: ""; flex: 1; height: 1.5px; background: var(--paper);
  }
  .advisory-brand__tagline {
    margin-top: 5px; font-size: 8.5px; font-weight: 600; letter-spacing: 0.3px;
  }
  .rule {
    position: absolute; left: 230px; right: 40px; top: 212px;
    height: 1.5px; background: var(--cyan);
  }
  .person { position: absolute; left: 50px; top: 186px; }
  .person__name { font-family: "Open Sans", sans-serif; font-weight: 700; font-size: 24px; }
  .person__role { color: var(--cyan); font-size: 16px; font-weight: 600; margin-top: -2px; }
  .contact {
    position: absolute; left: 50px; top: 256px;
    list-style: none; font-size: 16px; line-height: 26px;
  }
  .contact li { display: flex; align-items: center; gap: 12px; }
  .contact svg { width: 18px; height: 18px; flex: none; }
  .web-band {
    position: absolute; right: 0; bottom: 18px;
    width: 250px; height: 40px; background: var(--cyan);
    border-top-left-radius: 4px;
    display: flex; align-items: center; justify-content: center;
    font-size: 15px; color: var(--ink); font-weight: 600;
  }
  .paper-strip {
    position: absolute; right: 0; bottom: 0;
    width: 440px; height: 18px; background: var(--paper);
  }
</style>
</head>
<body>

<section class="card card--back" aria-label="Back of card">
  <div class="group-brand">
    <span class="group-brand__dot"></span>
    <span class="group-brand__name">Vela Norquist Group</span>
  </div>
  <p class="group-brand__tagline">Looking from outside the square</p>
  <p class="group-pillars">Advice <strong>Acumen</strong> Advocacy</p>
</section>

<section class="card card--front" aria-label="Front of card">
  <div class="advisory-brand">
    <span class="advisory-brand__dot"></span>
    <div>
      <div class="advisory-brand__name">Vela Norquist</div>
      <div class="advisory-brand__sub">ADVISORY</div>
      <div class="advisory-brand__tagline">Exceptional Intellect providing Compelling Solutions</div>
    </div>
  </div>

  <div class="rule"></div>

  <div class="person">
    <div class="person__name">Marcus Hale</div>
    <div class="person__role">Manager</div>
  </div>

  <ul class="contact">
    <li>
      <svg viewBox="0 0 18 18" aria-hidden="true"><circle cx="9" cy="9" r="9" fill="#22b3e0"/><rect x="6" y="4" width="6" height="10" rx="1" fill="none" stroke="#1b1b1c" stroke-width="1.5"/></svg>
      +55 4821 730 196
    </li>
    <li>
      <svg viewBox="0 0 18 18" aria-hidden="true"><circle cx="9" cy="9" r="9" fill="#22b3e0"/><rect x="4.5" y="5.5" width="9" height="7" fill="none" stroke="#1b1b1c" stroke-width="1.4"/><path d="M4.5 5.5 9 9.5l4.5-4" fill="none" stroke="#1b1b1c" stroke-width="1.4"/></svg>
      hello@velanorquist.com
    </li>
  </ul>

  <div class="web-band">www.velanorquist.com</div>
  <div class="paper-strip"></div>
</section>

</body>
</html>
```